Cosmetics Brand Logo and Bottle Label Design

We are creating a new cosmetics brand called "Nolan Whitby" and would like you to create an amazing logo and bottle label for this brand's new 100% pure argan oil product.
For the logo, we really like the logo's of Marin Calloway and Vessa. The text should be Sans Serif (without feet).
For the actual bottle label, please find attached labels of one of our competitors design which really like. We really like the simplicity and elegance of the design. The only difference is that our product will be using light turqoise as the brand color. Please feel free to add your own creativity into it as well.
Industry/Entity Type
Cosmetics
Logo Text
Nolan Whitby
Font styles to use

```html
<!DOCTYPE html>
<html lang="en">
<head>
<meta charset="UTF-8">
<title>Nolan Whitby – Argan Oil Label</title>
<link rel="stylesheet" href="https://fonts.googleapis.com/css2?family=Inter:wght@300;400&display=swap">
<style>
  :root {
    --page-bg: #ffffff;
    --label-teal: #2ec3ae;
    --label-teal-light: #3ccab6;
    --wave-aqua: #7ed6d6;
    --wave-sky: #a6dfe9;
    --ink: #25302f;
  }
  html, body {
    margin: 0;
    padding: 0;
    width: 816px;
    height: 1200px;
    overflow: hidden;
    background: var(--page-bg);
  }
  .label {
    position: absolute;
    left: 28px;
    top: 30px;
    width: 760px;
    height: 1140px;
    overflow: hidden;
    background: linear-gradient(180deg, var(--label-teal) 0%, var(--label-teal-light) 100%);
    font-family: "Inter", "Helvetica Neue", Arial, sans-serif;
  }
  .label__wave-area {
    position: absolute;
    left: 0;
    top: 0;
    width: 100%;
    height: 100%;
  }
  .label__brand {
    position: absolute;
    left: 86px;
    top: 1072px;
    margin: 0;
    transform: rotate(-90deg);
    transform-origin: 0 0;
    font-size: 104px;
    line-height: 104px;
    font-weight: 300;
    letter-spacing: 0.08em;
    color: var(--ink);
    white-space: nowrap;
    text-transform: uppercase;
  }
  .label__product {
    position: absolute;
    left: 238px;
    top: 1006px;
    margin: 0;
    font-size: 50px;
    line-height: 60px;
    font-weight: 400;
    color: var(--ink);
    white-space: nowrap;
  }
</style>
</head>
<body>
  <main class="label">
    <svg class="label__wave-area" viewBox="0 0 760 1140" preserveAspectRatio="none" role="img" aria-label="Soft flowing aqua wave graphic across the lower label">
      <defs>
        <linearGradient id="wave-area-fill" x1="0" y1="0" x2="0" y2="1">
          <stop offset="0" stop-color="#7ed6d6"/>
          <stop offset="1" stop-color="#a6dfe9"/>
        </linearGradient>
      </defs>
      <path d="M0 900 C 240 840, 500 760, 760 610 L 760 1140 L 0 1140 Z" fill="url(#wave-area-fill)"/>
    </svg>
    <h1 class="label__brand">Nolan&nbsp; Whitby</h1>
    <p class="label__product">100% pure argan oil</p>
  </main>
</body>
</html>
```